London Based Property Finding Company - have logo already

We find property for private purchasers and investors in London, UK.  We work for the BUYER, whereas estate agencies/real estate companies work for the seller. We offer a much more personalised service to UK and overseas purchasers.

We would like the following:

*A double sided business card

*A letterhead

We have attached two versions of the logo. Each logo style is set on two different coloured backgrounds. Please choose one of the two designs, whichever you prefer or feel more comfortable with, and produce one in black and one in white background.

This applies to both pieces of stationery.

THE BUSINESS CARD:

We would like the company name placed on its own on one side of the card and the contact details and what we do on the other.

e.g.

SIDE 1:

BRAMWELL PROPERTY FINDERS

SIDE 2:

Owen Bramwell

t: 0208 394 2261

m: +44(0)7940 318 472

e: info@bramwellpropertyfinders.co.uk

w: bramwellpropertyfinders.co.uk

London Property Finders and Search Agents

I will leave the layout up to you, but a minimalist layout is preferred. If you would like to put additional detial or design on the card then that is up to, but not specified.

It is optional to have the company name on side 2, but if you do use it, please make it smaller. than on the 1st side.

The design needs to be simple, professional and not too in your face.

If you are using the black background design on side 1 for the logo, then maybe a white backgounnd can be used on side 2 with a black typeface.

The type face for the contacts details should be sans serif standard typeface. Please experiment with the desciprtion.

-

THE LETTERHEAD;

You can experiment with the layout for the letterhead. e.g logo centre aligned on the top of the page with the contact details and address at the bottom of the page OR the logo, description running along a bar on the top of the page with the contact details and website address at the bottom. Please try and experiment with this, but the less 'busy', the better.

Here is info that needs to be on the letterhead.

Bramwell Property Finders

t: 0208 394 2261

m: +44(0)7940 318 472

(PLEASE NOTE; the below company info must be placed at the bottom of the page as a footer, in small text.)

Pemberly Holdings Ltd Trading as Bramwell Property Finders, a company registered in England & Wales, No.5917302 , Registered office is 41 Kelmscott House, Ashdown Lane, London, SW9 7QJ, t: 0208 394 2261, m: +44(0)7940 318 472, e: info@bramwellpropertyfinders.co.uk

Best of luck!

Thank you

Dear Designer,

I have now attached the supporting files to this brief.

Thanks,

Owen Bramwell
Bramwell Property Finders

```html
<!DOCTYPE html>
<html lang="en">
<head>
<meta charset="utf-8">
<title>Bramwell Property Finders – Stationery</title>
<link rel="stylesheet" href="https://fonts.googleapis.com/css2?family=Cinzel:wght@400&family=Open+Sans:wght@400&display=swap">
<style>
  :root {
    --ink: #0c0c0c;
    --paper: #ffffff;
    --backdrop: #e4e1dc;
    --footer-grey: #6a6a6a;
    --serif: "Cinzel", "Times New Roman", serif;
    --sans: "Open Sans", Arial, sans-serif;
  }
  * { box-sizing: border-box; margin: 0; padding: 0; }
  html, body { width: 1200px; height: 960px; overflow: hidden; }
  body { background: var(--backdrop); position: relative; font-family: var(--sans); }

  .shape { position: absolute; inset: 0; width: 100%; height: 100%; display: block; }
  .ink { fill: var(--ink); }
  .paper { fill: var(--paper); }

  /* Letterhead */
  .letterhead {
    position: absolute; left: 60px; top: 56px; width: 600px; height: 848px;
    background: var(--paper); box-shadow: 0 4px 18px rgba(0,0,0,.18);
  }
  .letterhead .brand {
    position: absolute; left: 22px; top: 29px;
    font-family: var(--serif); font-size: 16px; letter-spacing: 1px;
    color: var(--paper); line-height: 24px; white-space: nowrap;
  }
  .letterhead .contact-bar {
    position: absolute; left: 0; right: 0; top: 768px; height: 26px;
    display: flex; align-items: center; justify-content: center;
    font-size: 7.6px; color: var(--paper); white-space: nowrap;
  }
  .letterhead .legal {
    position: absolute; left: 0; right: 0; top: 800px;
    text-align: center; font-size: 6.6px; line-height: 10px; color: var(--footer-grey);
  }

  /* Business cards */
  .card {
    position: absolute; left: 710px; width: 440px; height: 284px;
    box-shadow: 0 4px 14px rgba(0,0,0,.2);
  }
  .card-front { top: 150px; }
  .card-back { top: 500px; }

  .card-front .brand {
    position: absolute; left: 46px; top: 126px;
    font-family: var(--serif); font-size: 22px; letter-spacing: 1px;
    color: var(--paper); white-space: nowrap;
  }

  .card-back .holder {
    position: absolute; right: 26px; top: 12px;
    font-family: var(--serif); font-size: 17px; letter-spacing: 3px;
    color: var(--ink); white-space: nowrap;
  }
  .card-back .details {
    position: absolute; right: 70px; top: 96px;
    list-style: none; text-align: right;
    font-size: 11.5px; line-height: 17px; color: var(--paper);
  }
  .card-back .tagline {
    position: absolute; left: 0; right: 0; bottom: 34px; text-align: center;
    font-size: 8.5px; letter-spacing: 1.5px; text-transform: uppercase; color: var(--paper);
  }
</style>
</head>
<body>

  <section class="letterhead">
    <svg class="shape" viewBox="0 0 600 848" aria-hidden="true">
      <polygon class="ink" points="0,22 600,22 600,38 346,38 324,60 0,60"/>
      <rect class="ink" x="0" y="768" width="600" height="26"/>
    </svg>
    <div class="brand">Bramwell Property Finders</div>
    <div class="contact-bar">t: 0208 394 2261 &nbsp;|&nbsp; m: +44(0)7940 318 472 &nbsp;|&nbsp; e: info@bramwellpropertyfinders.co.uk &nbsp;|&nbsp; w: bramwellpropertyfinders.co.uk</div>
    <p class="legal">Pemberly Holdings Ltd trading as Bramwell Property Finders, a company registered in England &amp; Wales, No.5917302<br>Registered office is 41 Kelmscott House, Ashdown Lane, London, SW9 7QJ</p>
  </section>

  <section class="card card-front">
    <svg class="shape" viewBox="0 0 440 284" aria-hidden="true">
      <rect class="ink" x="0" y="0" width="440" height="284"/>
      <polygon class="paper" points="250,0 440,0 440,36 282,36"/>
      <polygon class="paper" points="0,254 166,254 196,284 0,284"/>
    </svg>
    <div class="brand">Bramwell Property Finders</div>
  </section>

  <section class="card card-back">
    <svg class="shape" viewBox="0 0 440 284" aria-hidden="true">
      <rect class="ink" x="0" y="0" width="440" height="284"/>
      <polygon class="paper" points="150,0 440,0 440,42 184,42"/>
    </svg>
    <div class="holder">OWEN BRAMWELL</div>
    <ul class="details">
      <li>t: 0208 394 2261</li>
      <li>m: +44(0)7940 318 472</li>
      <li>e: info@bramwellpropertyfinders.co.uk</li>
      <li>w: bramwellpropertyfinders.co.uk</li>
    </ul>
    <p class="tagline">London Property Finders and Search Agents</p>
  </section>

</body>
</html>
```